ultra-minimalist business card

front (black background, matte):

omar k. nadiri
writer | photographer
get@omarknadiri.com

back (white background, matte):

a picture speaks a thousand words;
a word draws a thousand pictures.

www.omarknadiri.com

all text should be small (white or silver - as long as it shows against the black - on the front; black or gray - as long as it shows against the white - on the back).

feel free to get creative in terms of arrangement, alignment, and font type, but remember, the overall style is minimalist, so nothing too fancy, please.

thanks.

Industry/Entity Type

Business

```html
<!DOCTYPE html>
<html lang="en">
<head>
<meta charset="utf-8">
<title>Omar K. Nadiri — Business Card</title>
<link rel="stylesheet" href="https://fonts.googleapis.com/css2?family=Montserrat:wght@300;400;500;700&display=swap">
<style>
  :root {
    --backdrop: #e6e4e1;
    --card-white: #ffffff;
    --card-black: #050505;
    --ink-dark: #1a1a1a;
    --ink-light: #f2f2f2;
    --ink-silver: #b9b9b9;
    --shadow: rgba(0, 0, 0, 0.18);
  }
  * { margin: 0; padding: 0; box-sizing: border-box; }
  html, body {
    width: 1200px;
    height: 900px;
    overflow: hidden;
    background: var(--backdrop);
    font-family: "Montserrat", sans-serif;
  }
  .stage {
    position: relative;
    width: 1200px;
    height: 900px;
  }
  .card {
    position: absolute;
    width: 600px;
    height: 343px;
    box-shadow: 0 6px 18px var(--shadow);
    overflow: hidden;
  }

  /* Back: quote side */
  .card-back {
    left: 300px;
    top: 80px;
    background: var(--card-white);
    color: var(--ink-dark);
  }
  .quote-block {
    position: absolute;
    left: 0;
    right: 0;
    top: 150px;
    text-align: center;
  }
  .quote {
    display: inline-block;
    font-size: 13px;
    font-weight: 400;
    letter-spacing: 0.1px;
    white-space: nowrap;
    padding: 0 2px 4px;
    border-bottom: 2px solid var(--ink-dark);
  }
  .back-web {
    position: absolute;
    right: 68px;
    bottom: 46px;
    font-size: 13px;
    font-weight: 400;
  }
  .back-web strong { font-weight: 700; }

  /* Front: identity side */
  .card-front {
    left: 300px;
    top: 477px;
    background: var(--card-black);
    color: var(--ink-light);
  }
  .identity {
    position: absolute;
    left: 0;
    right: 0;
    top: 148px;
    display: flex;
    justify-content: center;
    align-items: center;
    gap: 14px;
  }
  .name-block { text-align: right; }
  .name {
    font-size: 14px;
    font-weight: 700;
    letter-spacing: 3px;
    text-transform: uppercase;
    line-height: 1.25;
  }
  .role {
    font-size: 14px;
    font-weight: 300;
    letter-spacing: 0.4px;
    line-height: 1.3;
  }
  .divider {
    width: 1px;
    height: 42px;
    background: var(--ink-silver);
  }
  .contact-list { list-style: none; }
  .contact-item {
    display: flex;
    align-items: center;
    gap: 8px;
    font-size: 13.5px;
    font-weight: 300;
    line-height: 1.45;
  }
  .contact-item strong { font-weight: 700; }
  .contact-icon { width: 11px; height: 11px; flex: none; }
</style>
</head>
<body>
<main class="stage">

  <section class="card card-back" aria-label="Card back">
    <div class="quote-block">
      <p class="quote">a picture speaks a thousand words; a word draws a thousand pictures</p>
    </div>
    <p class="back-web">www.<strong>omarknadiri</strong>.com</p>
  </section>

  <section class="card card-front" aria-label="Card front">
    <div class="identity">
      <div class="name-block">
        <h1 class="name">Omar K. Nadiri</h1>
        <p class="role">Writer | Photographer</p>
      </div>
      <div class="divider"></div>
      <ul class="contact-list">
        <li class="contact-item">
          <svg class="contact-icon" viewBox="0 0 12 12" aria-hidden="true">
            <rect x="0.5" y="2" width="11" height="8" fill="var(--ink-light)"/>
            <path d="M0.8 2.4 L6 6.6 L11.2 2.4" fill="none" stroke="var(--card-black)" stroke-width="1"/>
          </svg>
          <span>get@omarknadiri.com</span>
        </li>
        <li class="contact-item">
          <svg class="contact-icon" viewBox="0 0 12 12" aria-hidden="true">
            <circle cx="6" cy="6" r="5.2" fill="none" stroke="var(--ink-light)" stroke-width="1.2"/>
            <ellipse cx="6" cy="6" rx="2.2" ry="5.2" fill="none" stroke="var(--ink-light)" stroke-width="1"/>
            <line x1="0.8" y1="6" x2="11.2" y2="6" stroke="var(--ink-light)" stroke-width="1"/>
          </svg>
          <span>www.<strong>omarknadiri</strong>.com</span>
        </li>
      </ul>
    </div>
  </section>

</main>
</body>
</html>
```